Corvale Homes

To produce a business card design for our newly established house building and development company, We have had a logo design done please see attached, our slogan is "Shaping the home you deserve"
Contact Information for Business Card
Adress on card needs to Read - 58 Elmsworth Lane, Ashby Vale, Wrenshire WV12 4QT. Director name Dean Vascotti
Requirements
Must have
- Web adress is www.corvale-homes.co.uk
- Email address is info@corvale-homes.co.uk
- phone number 07700 900417

```html
<!DOCTYPE html>
<html lang="en">
<head>
<meta charset="utf-8">
<title>Corvale Homes – Business Card</title>
<link rel="stylesheet" href="https://fonts.googleapis.com/css2?family=Tinos:wght@400;700&display=swap">
<style>
  :root {
    --page-bg: #e4e3e4;
    --card-white: #ffffff;
    --ink: #4a4a4a;
    --ink-soft: #6b6b6b;
    --rule: #cfcfcf;
    --logo-ink: #ffffff;
  }
  html, body {
    margin: 0;
    width: 1200px;
    height: 1200px;
    overflow: hidden;
    background: var(--page-bg);
  }
  .sheet {
    width: 1200px;
    height: 1200px;
    display: flex;
    flex-direction: column;
    align-items: center;
    justify-content: center;
    gap: 60px;
  }
  .card { width: 900px; height: 514px; display: block; }
  .card-text { font-family: "Tinos", "Times New Roman", serif; fill: var(--ink); }
  .holder-name { font-size: 38px; letter-spacing: 5px; }
  .holder-role { font-size: 21px; fill: var(--ink-soft); }
  .contact-line { font-size: 21px; fill: var(--ink-soft); }
  .tagline-front { font-size: 26px; letter-spacing: 3px; }
  .brand-name { font-family: "Tinos", "Times New Roman", serif; font-weight: 700; font-size: 62px; letter-spacing: 4px; fill: var(--logo-ink); }
  .brand-tagline { font-family: "Tinos", "Times New Roman", serif; font-size: 15px; letter-spacing: 6px; fill: var(--logo-ink); }
  .icon { fill: var(--ink-soft); }
</style>
</head>
<body>
<main class="sheet">

  <svg class="card card-front" viewBox="0 0 900 514" aria-label="Business card front">
    <defs>
      <clipPath id="front-shape"><rect width="900" height="514" rx="44"/></clipPath>
      <linearGradient id="front-grey" x1="0" y1="0" x2="1" y2="1">
        <stop offset="0" stop-color="#7a7b7c"/>
        <stop offset="1" stop-color="#8f9091"/>
      </linearGradient>
    </defs>
    <g clip-path="url(#front-shape)">
      <rect width="900" height="514" fill="url(#front-grey)"/>
      <polygon fill="var(--card-white)"
        points="0,514 0,384 110,384 350,170 660,170 660,44 790,44 790,140 900,140 900,514"/>
      <line x1="0" y1="448" x2="900" y2="448" stroke="var(--rule)" stroke-width="1.5"/>
      <line x1="0" y1="470" x2="900" y2="470" stroke="var(--rule)" stroke-width="1"/>
    </g>

    <text class="card-text holder-name" x="520" y="232" text-anchor="middle">DEAN VASCOTTI</text>
    <text class="card-text holder-role" x="460" y="270" text-anchor="end">Director</text>
    <line x1="474" y1="252" x2="474" y2="274" stroke="var(--ink-soft)" stroke-width="1.5"/>
    <path class="icon" d="M488 256c0 8 6 14 14 14l3-3-4-4-2 2c-3-1-5-3-6-6l2-2-4-4z"/>
    <text class="card-text contact-line" x="512" y="270">07700 900417</text>

    <text class="card-text contact-line" x="466" y="325" text-anchor="end">58 Elmsworth Lane, Ashby Vale</text>
    <text class="card-text contact-line" x="488" y="357" text-anchor="end">Wrenshire WV12 4QT</text>
    <path class="icon" d="M474 312a7 7 0 0 1 14 0c0 6-7 13-7 13s-7-7-7-13zm7-2a2 2 0 1 0 0.01 0z"/>

    <line x1="504" y1="306" x2="504" y2="368" stroke="var(--rule)" stroke-width="1.5"/>

    <circle class="icon" cx="530" cy="318" r="8"/>
    <text class="card-text contact-line" x="548" y="325">www.corvale-homes.co.uk</text>
    <rect class="icon" x="522" y="344" width="16" height="11"/>
    <text class="card-text contact-line" x="548" y="357">info@corvale-homes.co.uk</text>

    <line x1="260" y1="392" x2="820" y2="392" stroke="var(--rule)" stroke-width="1.5"/>
    <text class="card-text tagline-front" x="540" y="430" text-anchor="middle">SHAPING THE HOME YOU DESERVE</text>
  </svg>

  <svg class="card card-back" viewBox="0 0 900 514" aria-label="Business card back">
    <defs>
      <clipPath id="back-shape"><rect width="900" height="514" rx="44"/></clipPath>
      <linearGradient id="back-base" x1="0" y1="0" x2="1" y2="1">
        <stop offset="0" stop-color="#6f7072"/>
        <stop offset="1" stop-color="#3f4042"/>
      </linearGradient>
      <linearGradient id="back-house" x1="0" y1="0" x2="1" y2="1">
        <stop offset="0" stop-color="#8c8d8e"/>
        <stop offset="1" stop-color="#5c5d5f"/>
      </linearGradient>
    </defs>
    <g clip-path="url(#back-shape)">
      <rect width="900" height="514" fill="url(#back-base)"/>
      <polygon fill="url(#back-house)"
        points="0,0 900,0 900,140 790,140 790,44 660,44 660,170 350,170 110,384 0,384"/>
    </g>
    <text class="brand-name" x="520" y="300" text-anchor="middle">CORVALE HOMES</text>
    <line x1="300" y1="324" x2="740" y2="324" stroke="var(--logo-ink)" stroke-width="1.5"/>
    <text class="brand-tagline" x="520" y="350" text-anchor="middle">SHAPING THE HOME YOU DESERVE</text>
  </svg>

</main>
</body>
</html>
```